Self-Publisher seeking a professional Book Cover design

Paperback novel, science-fiction/mind-fiction. Title “Tovald’s Hollow”. Will be published via Pellow PBX and must meet their sizing requirements for a Book Cover (‘the spine”). (The book is 362 pages). The overall concept of design should be relatively simple, playing with themes of dark/blackness/space/unconscious/insanity-themes. Initially I had in mind a dark cover with something floating small and distant in the darkness like a sort of “space-cocoon”/hibernation-tank for an astronaut. (just something to get started thinking with). I am very open to any concepts.

From the back cover:
“In the year 3438, a discovery of a lifetime is made, and promises new light for a whole new generation of mankind which has permanently stagnated, becoming little more than slaves to their own technology which itself has already plateaued. Life goes on, yet for man, it stopped over a millennia ago. A secret project begun in the Ancient-American West in the year 1947, has catastrophic implications for the modern people’s of 3438. A discovery in space that lay apparently dormant for over a thousand years, mysteriously hidden from mankind’s ever evolving technological grasp, leads to a culture-shattering revelation that can only have one outcome. Chaos. …”

Target Market(s)

25-45 yr.

Industry/Entity Type

science-fiction, mind-bending, esotericism, psychological, space,

Font styles to use
Serif

Colors

Designer to choose colors to be used in the design.

Requirements
Must have
• darkness, with perhaps elements of bright light???
Should not have
• nothing too colorful. think, “unconscious”.

```html
<!DOCTYPE html>
<html lang="en">
<head>
<meta charset="utf-8">
<title>Tovald’s Hollow — Paperback Cover</title>
<link rel="stylesheet" href="https://fonts.googleapis.com/css2?family=Josefin+Sans:wght@300;400;600&family=Arimo:ital,wght@0,400;1,400;1,700&display=swap">
<style>
  :root {
    --backdrop: #a6a6a6;
    --void: #030304;
    --ink: #ffffff;
    --ink-soft: #e9e9ec;
    --glow-pale: #cfe2f0;
    --glow-blue: #6f8fb3;
    --glow-violet: #4a3e63;
  }
  * { margin: 0; padding: 0; box-sizing: border-box; }
  html, body { width: 1200px; height: 949px; overflow: hidden; background: var(--backdrop); }
  .cover {
    position: absolute; left: 78px; top: 114px; width: 1044px; height: 722px;
    background: var(--void);
    box-shadow: 12px 16px 22px rgba(0,0,0,.45);
    overflow: hidden; color: var(--ink);
  }
  .starfield {
    position: absolute; inset: 0;
    background: radial-gradient(ellipse at 30% 40%, #0d0d10 0%, var(--void) 70%);
  }
  .vortex-art {
    position: absolute; left: 620px; top: 90px; width: 424px; height: 560px;
    background:
      radial-gradient(ellipse 48% 40% at 108% 42%, var(--glow-pale) 0%, var(--glow-blue) 28%, var(--glow-violet) 48%, rgba(20,20,30,.6) 66%, transparent 80%);
  }
  .title-kicker {
    position: absolute; font-family: 'Josefin Sans', sans-serif; font-weight: 300;
    letter-spacing: .48em; text-align: center; white-space: nowrap;
  }
  .title-main {
    position: absolute; font-family: 'Josefin Sans', sans-serif; font-weight: 600;
    letter-spacing: .14em; text-align: center; white-space: nowrap; line-height: 1;
  }
  /* back cover */
  .back-kicker { left: 121px; width: 240px; top: 73px; font-size: 18px; }
  .back-title { left: 101px; width: 280px; top: 95px; font-size: 40px; }
  .blurb {
    position: absolute; left: 61px; top: 141px; width: 361px;
    font-family: 'Arimo', sans-serif; font-size: 9.4px; line-height: 12.1px;
    text-align: justify; color: var(--ink-soft);
  }
  .blurb p { margin-bottom: 11.5px; }
  .blurb p:first-child { margin-bottom: 23px; }
  .blurb em { font-weight: 700; }
  .pull-quote {
    position: absolute; left: 60px; top: 527px; width: 362px; height: 43px;
    border: 1px solid var(--ink);
    font-family: 'Arimo', sans-serif; font-style: italic; font-size: 14.5px;
    text-align: center; padding-top: 12px;
  }
  .pull-quote cite {
    position: absolute; right: 44px; bottom: -6px; padding: 0 7px;
    background: var(--void); font-style: normal; font-size: 7.5px;
  }
  .imprint { position: absolute; left: 54px; top: 612px; font-family: 'Arimo', sans-serif; }
  .imprint-mark { display: flex; align-items: center; gap: 4px; font-size: 8px; }
  .imprint-mark span.square { width: 10px; height: 10px; background: var(--ink); }
  .imprint-line { margin-top: 36px; font-size: 5.5px; }
  .imprint-web { margin-top: 7px; font-size: 8.6px; letter-spacing: .02em; }
  .isbn-panel { position: absolute; left: 318px; top: 635px; width: 107px; height: 48px; background: var(--ink); }
  /* spine */
  .spine-title, .spine-author {
    position: absolute; writing-mode: vertical-rl; font-family: 'Josefin Sans', sans-serif; white-space: nowrap;
  }
  .spine-title { left: 490px; top: 76px; display: flex; flex-direction: row-reverse; gap: 2px; }
  .spine-title .kicker { font-weight: 300; font-size: 15px; letter-spacing: .42em; }
  .spine-title .main { font-weight: 600; font-size: 37px; letter-spacing: .12em; line-height: 1; }
  .spine-author { left: 497px; top: 402px; display: flex; flex-direction: row-reverse; gap: 6px; font-weight: 300; font-size: 13px; letter-spacing: .28em; }
  .spine-mark { position: absolute; left: 498px; top: 650px; width: 11px; height: 11px; background: var(--ink); }
  /* front cover */
  .front-kicker { left: 648px; width: 320px; top: 75px; font-size: 27px; }
  .front-title { left: 628px; width: 360px; top: 110px; font-size: 60px; }
  .front-author {
    position: absolute; left: 638px; width: 340px; top: 646px; text-align: center;
    font-family: 'Josefin Sans', sans-serif; font-weight: 300; letter-spacing: .22em; line-height: 1.3;
  }
  .front-author .the { font-size: 15px; display: block; }
  .front-author .name { font-size: 18px; display: block; }
</style>
</head>
<body>
  <section class="cover" aria-label="Paperback cover spread for Tovald’s Hollow">
    <div class="starfield"></div>
    <div class="vortex-art" role="img" aria-label="Small satellite drifting beside a swirling pale blue and violet vortex of light in deep space"></div>

    <!-- back cover -->
    <div class="title-kicker back-kicker">TOVALD’S</div>
    <div class="title-main back-title">HOLLOW</div>
    <div class="blurb">
      <p>In the year 3438, a discovery of a lifetime is made which promises new light for a future generation of mankind that has permanently stagnated, having become little more than slaves to their own technology which itself has already plateaued. Life goes on, and yet for man, it stopped <em><i>over a millennia ago</i></em>.</p>
      <p>A secret project begun in the Ancient-American West in the year 1947, has catastrophic implications for the modern People’s of the future. This unbelievable discovery in space, an artifact from a dead culture that lay apparently dormant for over a millennia, mysteriously hidden from mankind’s ever-evolving technological grasp, leads to a culture-shattering revelation that can only have one outcome. <em><i>Chaos</i></em>.</p>
      <p>What was once lost in the confusion of a post global conflict of prophesied proportion, is found hiding in plain sight.</p>
      <p>The revelations of an Ancient-American astronaut’s journey above the earth alone, bring culture melting and empire crumbling consequences to a hopeless humanity sheltered and enslaved by the rulers of the time whom seem set on hiding an ancient truth at all costs. The Capital’s Guard may have no choice but to risk reigniting the ancient flames of war, to prevent a change over three-thousand years in the making.</p>
      <p>A truth found, and ancient dreams of the early 21st century are finally realized. But at what insane cost? And who is willing to pay them? The long prophesied Golden Age is seen on the horizon, but a dark shadow yet looms over an even darker mind of mankind. What feared insanity must man embrace, to find a new way forward?</p>
      <p>It is complicated, as man is. It is shocking, as man can be, and, it’s embarrassing and confusing to the intellect, when considered sincerely. This may be his journey, but the story, I assure you, is ours.</p>
    </div>
    <blockquote class="pull-quote">The Light indeed shines brighter, in the dark.<cite>The Lanternwright</cite></blockquote>
    <div class="imprint">
      <div class="imprint-mark"><span class="square"></span>Lanternwright</div>
      <div class="imprint-line">[LUMEN-II]editions;</div>
      <div class="imprint-web">LANTERNWRIGHTPRESS.COM</div>
    </div>
    <div class="isbn-panel"></div>

    <!-- spine -->
    <div class="spine-title"><span class="kicker">TOVALD’S</span><span class="main">HOLLOW</span></div>
    <div class="spine-author"><span>THE</span><span>LANTERNWRIGHT</span></div>
    <div class="spine-mark"></div>

    <!-- front cover -->
    <div class="title-kicker front-kicker">TOVALD’S</div>
    <div class="title-main front-title">HOLLOW</div>
    <div class="front-author"><span class="the">THE</span><span class="name">LANTERNWRIGHT</span></div>
  </section>
</body>
</html>
```